Basic Website Design for Healthcare Services Startup

We need a professional designer to take our existing basic mobile website and create professional mobile and desktop website designs. We need the designer to use the existing content and page structure at our current mobile website (http://www.valtrix.com/phone/index.html) for the new design. Let us know if you have suggestions on how we can improve the site map.

The design needs to feel contemporary and clean. We need to convey a very professional operation that embraces technology. PLEASE refer to the attached brochure to understand the style and feel we want the website to have.

We want to start small and quickly iterate to a larger, final product. Initial submissions should only include a desktop homepage and a mobile homepage. I WILL PROVIDE INITIAL FEEDBACK AND COMMIT MONEY TO THE PROJECT BEFORE ASKING DESIGNERS TO COMPLETE A FULL DESIGN FOR THE ENTIRE DESKTOP AND MOBILE SITE.

We are happy to email you any stock photos you see on our current site. Please feel free to ask questions.

Please stay close to our current color scheme, but feel free to add new colors to our palette as needed.
Our blue is: #7CD9DA
Our gray is: #585751

Thanks Designers!!

Target Market(s)

Males, Ages 18-24

Industry/Entity Type

Health Care

Number of Pages Required

5+ page

Font styles to use
Sans Serif

Requirements
Must have
• -Final design must contain all content on www.valtrix.com/phone/ website.
• -All graphics/designs/content must be easily accessible in the final deliverable so we can import it into Adobe Muse for development.
• -Must be designed in Adobe.
• -Please specify different states: normal, rollover, active, etc.
• ***UPDATE***
• Thank you everyone for your submissions! I am very happy with the quality of submissions so I will commit to the guarantee. Please focus on my comments and submit your best 2 or 3 designers. I want to give strong feedback to all designers and it is difficult when there are many different combinations of the same design elements.
• A few quick notes to help guide future submissions:
• 1.) PICTURE CONTENT: right now the focus is on designing the landing page for our donors, so the audience is 18-24 males. We want a few medical pictures, but we mostly want to connect with our donor base. Please save the pictures of doctors for the HOSPITAL PAGE. For this main page we either want to see black or hispanic people donating blood, having fun, or being with friends and loved ones.
• 2.) HOMEPAGE CONTENT: Please use the content on www.valtrix.com/phone/index.html for homepage content guidance. We do not want to include a lot of the hospital brochure content on the homepage we want that content on the HOSPITAL PAGE).
• 3.) BLOG CONTENT: Add a section for articles/blog content. We want to feature the most recent post and small previews of the previous 2 or 3 articles.
• 4.) SOCIAL: we want our social media icons to be prominent. Either in the header or at the top of the page.
• 5.) NO PARTNERS: we don't want to include our partners on the donor homepage.
• ***UPDATE***
• Hi everyone, quick clarification. The final winner will need to include all these pages. Most of them should be very quick because they do not have a lot of content on them. Please focus on the donor homepage. I will approve the look and feel before asking you to create the rest of the pages. Please note I need both Desktop and
• Mobile versions of these designs:
• Pages Needed in final design:
• -Homepage <= 85% of design work should be on this page
• -Registration
• -Hospital
• -Donor Eligibility
• -How Valtrix Works
• -Learn About PBSC Donation
• -Learn About Blood Cancer
• -About Us
Nice to have
• -Nice to have an idea how we can make your design responsive.
Should not have
• None.

```html
<!DOCTYPE html>
<html lang="en">
<head>
<meta charset="utf-8">
<title>Valtrix – Earn Money While You Save a Life</title>
<link href="https://fonts.googleapis.com/css2?family=Lato:ital,wght@0,300;0,400;0,700;1,400&display=swap" rel="stylesheet">
<style>
  :root {
    --teal: #7cd9da;
    --teal-mid: #76c9cb;
    --teal-dark: #5fb8bb;
    --gray: #585751;
    --gray-line: #6c6b65;
    --ink: #4a4a47;
    --text: #5d5d5a;
    --muted: #b9b8b2;
    --white: #ffffff;
  }
  * { box-sizing: border-box; margin: 0; padding: 0; }
  html, body { width: 1200px; height: 2287px; overflow: hidden; }
  body { font-family: "Lato", sans-serif; color: var(--text); background: var(--white); position: relative; }
  a { color: inherit; text-decoration: none; }

  /* Header */
  .site-header { position: relative; height: 110px; background: var(--white); }
  .brand { position: absolute; left: 37px; top: 26px; display: flex; align-items: center; gap: 14px; }
  .brand-dot { width: 44px; height: 44px; border: 2px solid var(--teal); border-radius: 50%; }
  .brand-name { font-size: 34px; font-weight: 300; letter-spacing: 5px; color: var(--ink); }
  .social-top { position: absolute; right: 66px; top: 24px; display: flex; gap: 16px; }
  .social-square { width: 29px; height: 29px; background: var(--gray); display: block; }
  .social-square.is-teal { background: var(--teal); }
  .main-nav { position: absolute; left: 267px; top: 69px; display: flex; height: 38px; }
  .main-nav a { font-size: 13px; font-weight: 400; text-transform: uppercase; color: var(--ink); padding: 0 16px; line-height: 38px; letter-spacing: .2px; }
  .main-nav a.is-active { background: var(--teal); color: var(--white); padding: 0 18px; }

  /* Hero */
  .hero { position: relative; height: 489px; color: var(--white); text-align: center; overflow: hidden; }
  .hero-photo { position: absolute; inset: 0; background: linear-gradient(100deg, #3c4a4f 0%, #3f6c6f 45%, #5b9c98 75%, #7cb7b0 100%); }
  .hero-tint { position: absolute; inset: 0; background: rgba(96, 176, 172, .25); }
  .hero-content { position: relative; padding-top: 200px; }
  .hero-title { font-size: 50px; font-weight: 300; letter-spacing: 1px; }
  .hero-sub { font-size: 27px; font-weight: 300; margin-top: 18px; }
  .btn-outline-light { display: inline-block; margin-top: 44px; border: 2px solid var(--white); border-radius: 26px; padding: 0 28px; height: 50px; line-height: 46px; font-size: 21px; font-weight: 400; }
  .hero-arrow { position: absolute; top: 337px; width: 32px; height: 32px; border: 2px solid rgba(255,255,255,.8); border-radius: 50%; }
  .hero-arrow svg { display: block; margin: 7px auto 0; }
  .hero-arrow.prev { left: 37px; }
  .hero-arrow.next { right: 49px; }

  /* Section headings */
  .section-title { font-size: 30px; font-weight: 400; text-transform: uppercase; color: var(--ink); }
  .section-title span { color: var(--teal-dark); }
  .title-rule { width: 155px; height: 1px; background: var(--teal); margin-top: 16px; }

  /* Get involved */
  .get-involved { height: 215px; padding: 32px 37px 0; }
  .involve-actions { display: flex; gap: 30px; margin-top: 29px; }
  .involve-btn { width: 543px; height: 60px; border-radius: 30px; display: flex; align-items: center; padding-left: 6px; font-size: 23px; text-transform: uppercase; }
  .involve-btn .icon-box { width: 68px; height: 48px; border-radius: 24px 4px 4px 24px; display: flex; align-items: center; justify-content: center; margin-right: 30px; }
  .involve-btn.is-primary { background: var(--teal); color: var(--white); font-weight: 700; }
  .involve-btn.is-primary .icon-box { background: var(--white); }
  .involve-btn.is-secondary { border: 2px solid var(--gray); color: var(--ink); }
  .involve-btn.is-secondary .icon-box { background: var(--gray); }

  /* Need section */
  .need { height: 526px; background: var(--teal-mid); color: var(--white); padding: 47px 37px 0; position: relative; }
  .need .section-title { color: var(--white); font-size: 29px; }
  .need .title-rule { background: var(--white); width: 156px; margin-top: 22px; }
  .need-list { list-style: none; margin-top: 32px; width: 640px; }
  .need-list li { position: relative; padding-left: 36px; font-size: 19px; line-height: 27px; margin-bottom: 27px; }
  .need-list li svg { position: absolute; left: 0; top: 5px; }
  .btn-outline-small { position: absolute; left: 37px; top: 446px; width: 209px; height: 40px; border: 2px solid var(--white); border-radius: 20px; text-align: center; line-height: 36px; font-size: 20px; font-weight: 700; }
  .need-video { position: absolute; left: 704px; top: 146px; width: 447px; height: 340px; background: #111; }
  .need-video .video-frame { position: absolute; left: 0; right: 0; top: 10px; bottom: 10px; background: linear-gradient(120deg, #3a3836 0%, #55514d 50%, #6e6a66 100%); }
  .need-video .play { position: absolute; left: 186px; top: 133px; }

  /* Testimonials */
  .testimonials { height: 328px; background: var(--gray); padding: 34px 37px 0; position: relative; }
  .testimonials .section-title { color: var(--teal); font-size: 30px; }
  .testimonials .title-rule { width: 155px; background: var(--teal); }
  .avatar { position: absolute; left: 67px; top: 119px; width: 138px; height: 138px; border-radius: 50%; border: 3px solid var(--white); background: linear-gradient(150deg, #c8a58e, #8c6a58); }
  .quote-badge { position: absolute; left: 37px; top: 122px; width: 62px; height: 62px; border-radius: 50%; background: var(--teal); border: 3px solid var(--white); color: var(--white); font-size: 44px; font-weight: 700; text-align: center; line-height: 66px; }
  .quote { position: absolute; left: 232px; top: 140px; width: 930px; font-size: 18px; font-style: italic; line-height: 31px; color: var(--muted); }
  .quote-author { position: absolute; left: 232px; top: 222px; font-size: 18px; color: var(--teal); }
  .slider-dots { position: absolute; right: 52px; top: 245px; display: flex; gap: 3px; }

  /* Blog */
  .blog { height: 397px; padding: 34px 37px 0; }
  .blog-grid { display: flex; gap: 29px; margin-top: 46px; }
  .blog-card { width: 352px; }
  .blog-photo { height: 163px; }
  .blog-photo.color { background: linear-gradient(110deg, #2a9ea0 0%, #6fc2c4 45%, #e6dfd8 70%, #c9b8b0 100%); }
  .blog-photo.mono-a { background: linear-gradient(160deg, #e9e9e9 0%, #a6a6a6 55%, #6d6d6d 100%); }
  .blog-photo.mono-b { background: linear-gradient(160deg, #f2f2f2 0%, #bdbdbd 50%, #7a7a7a 100%); }
  .blog-meta { display: flex; gap: 14px; margin-top: 12px; }
  .date-box { width: 57px; height: 68px; border: 2px solid var(--gray); text-align: center; flex-shrink: 0; color: var(--gray); }
  .date-box .day { font-size: 24px; font-weight: 700; line-height: 42px; }
  .date-box .month { font-size: 14px; border-top: 2px solid var(--gray); line-height: 22px; }
  .blog-card.is-featured .date-box { border-color: var(--teal-dark); color: var(--teal-dark); }
  .blog-card.is-featured .date-box .month { border-color: var(--teal-dark); }
  .blog-excerpt { font-size: 17px; line-height: 26px; padding-top: 6px; color: var(--text); }
  .blog-card.is-featured .blog-excerpt { color: var(--teal-dark); }

  /* Footer */
  .site-footer { height: 221px; background: var(--gray); padding: 0 37px; color: var(--muted); position: relative; }
  .footer-nav { text-align: center; font-size: 15px; padding-top: 20px; height: 58px; border-bottom: 1px solid var(--gray-line); }
  .footer-nav a { color: var(--muted); }
  .footer-nav a.is-active { color: var(--teal); }
  .footer-nav .sep { margin: 0 9px; }
  .contact-row { display: flex; height: 109px; border-bottom: 1px solid var(--gray-line); padding-top: 26px; }
  .contact-item { display: flex; gap: 14px; }
  .contact-item.address { width: 478px; }
  .contact-item.phone { width: 285px; }
  .contact-icon { width: 62px; height: 58px; border: 1px solid var(--teal); display: flex; align-items: center; justify-content: center; }
  .contact-label { font-size: 15px; font-weight: 700; color: var(--teal); text-transform: uppercase; margin-top: 4px; }
  .contact-value { font-size: 16px; margin-top: 10px; }
  .footer-bottom { display: flex; justify-content: space-between; align-items: center; height: 52px; font-size: 14px; }
  .social-footer { display: flex; gap: 22px; }
  .social-footer .social-square { width: 26px; height: 26px; background: #6a6963; }
  .social-footer .social-square.is-teal { background: var(--teal); }
</style>
</head>
<body>

<header class="site-header">
  <a class="brand" href="#"><span class="brand-dot"></span><span class="brand-name">VALTRIX</span></a>
  <div class="social-top">
    <a class="social-square is-teal" href="#" aria-label="Social profile"></a>
    <a class="social-square" href="#" aria-label="Social profile"></a>
    <a class="social-square" href="#" aria-label="Social profile"></a>
  </div>
  <nav class="main-nav">
    <a class="is-active" href="#">Home</a>
    <a href="#">About Us</a>
    <a href="#">Get Involved</a>
    <a href="#">Why $2,000?</a>
    <a href="#">How Valtrix Works</a>
    <a href="#">Donor Eligibility</a>
    <a href="#">Contact Us</a>
  </nav>
</header>

<section class="hero">
  <div class="hero-photo" role="img" aria-label="Photo of a young donor relaxing in a clinic chair during a stem cell donation"></div>
  <div class="hero-tint"></div>
  <a class="hero-arrow prev" href="#" aria-label="Previous slide"><svg width="12" height="14" viewBox="0 0 12 14"><path d="M8 1 2 7l6 6" fill="none" stroke="#fff" stroke-width="2"/></svg></a>
  <a class="hero-arrow next" href="#" aria-label="Next slide"><svg width="12" height="14" viewBox="0 0 12 14"><path d="M4 1l6 6-6 6" fill="none" stroke="#fff" stroke-width="2"/></svg></a>
  <div class="hero-content">
    <h1 class="hero-title">EARN MONEY WHILE YOU SAVE A LIFE</h1>
    <p class="hero-sub">Donors will receive $2,000 for each donation</p>
    <a class="btn-outline-light" href="#">REGISTER TODAY</a>
  </div>
</section>

<section class="get-involved">
  <h2 class="section-title">Get <span>Involved</span></h2>
  <div class="title-rule"></div>
  <div class="involve-actions">
    <a class="involve-btn is-primary" href="#">
      <span class="icon-box"><svg width="38" height="32" viewBox="0 0 38 32"><path d="M19 30 5 16C-1 10 4 1 11 3c4 1 6 4 8 6 2-2 4-5 8-6 7-2 12 7 6 13z" fill="none" stroke="#7cd9da" stroke-width="2.5"/><path d="M4 16h9l3-6 4 11 3-5h11" fill="none" stroke="#7cd9da" stroke-width="2.5"/></svg></span>
      Become a H.E.R.O
    </a>
    <a class="involve-btn is-secondary" href="#">
      <span class="icon-box"><svg width="28" height="28" viewBox="0 0 28 28"><rect x="3" y="3" width="22" height="22" rx="3" fill="none" stroke="#fff" stroke-width="2.5"/><path d="M14 8v12M8 14h12" stroke="#fff" stroke-width="2.5"/></svg></span>
      Organize a Donor Drive
    </a>
  </div>
</section>

<section class="need">
  <h2 class="section-title">You are desperately needed to save a life</h2>
  <div class="title-rule"></div>
  <ul class="need-list">
    <li><svg width="22" height="18" viewBox="0 0 22 18"><path d="M1 1l20 8-20 8 5-8z" fill="none" stroke="#fff" stroke-width="1.6"/></svg>1 in 3 minority blood cancer patients cannot find a donor</li>
    <li><svg width="22" height="18" viewBox="0 0 22 18"><path d="M1 1l20 8-20 8 5-8z" fill="none" stroke="#fff" stroke-width="1.6"/></svg>You might be the ONLY person that can save someone’s life</li>
    <li><svg width="22" height="18" viewBox="0 0 22 18"><path d="M1 1l20 8-20 8 5-8z" fill="none" stroke="#fff" stroke-width="1.6"/></svg>Matches usually occur between people of the same race</li>
    <li><svg width="22" height="18" viewBox="0 0 22 18"><path d="M1 1l20 8-20 8 5-8z" fill="none" stroke="#fff" stroke-width="1.6"/></svg>Over 8,000 Americans need a blood stem cell donation each year</li>
    <li><svg width="22" height="18" viewBox="0 0 22 18"><path d="M1 1l20 8-20 8 5-8z" fill="none" stroke="#fff" stroke-width="1.6"/></svg>Valtrix recruits donors for African American, Asian, and Hispanic communities</li>
  </ul>
  <a class="btn-outline-small" href="#">Register Today</a>
  <div class="need-video">
    <div class="video-frame" role="img" aria-label="Video still of a donor telling his story at home"></div>
    <svg class="play" width="74" height="74" viewBox="0 0 74 74"><circle cx="37" cy="37" r="37" fill="rgba(255,255,255,.9)"/><path d="M29 21l24 16-24 16z" fill="#2f2e2c"/></svg>
  </div>
</section>

<section class="testimonials">
  <h2 class="section-title">Testimonials</h2>
  <div class="title-rule"></div>
  <div class="avatar" role="img" aria-label="Portrait of the donor quoted"></div>
  <div class="quote-badge">“</div>
  <p class="quote">"Matching as a donor has been an honor and a privilege. There are no words to describe the miraculous feeling that comes with having the ability to provide someone with the opportunity for a second chance at life."</p>
  <p class="quote-author">- Marisol</p>
  <div class="slider-dots">
    <svg width="20" height="12" viewBox="0 0 20 12"><path d="M0 4 10 0l10 8-10 4z" fill="#7cd9da"/></svg>
    <svg width="20" height="12" viewBox="0 0 20 12"><path d="M0 4 10 0l10 8-10 4z" fill="#9b9a94"/></svg>
    <svg width="20" height="12" viewBox="0 0 20 12"><path d="M0 4 10 0l10 8-10 4z" fill="#9b9a94"/></svg>
  </div>
</section>

<section class="blog">
  <h2 class="section-title">Latest <span>Blog</span></h2>
  <div class="blog-grid">
    <article class="blog-card is-featured">
      <div class="blog-photo color" role="img" aria-label="Photo of a medical team in scrubs"></div>
      <div class="blog-meta">
        <div class="date-box"><div class="day">26</div><div class="month">FEB</div></div>
        <p class="blog-excerpt">Lorem ipsum dolor sit amet cons am etur adipiscing elit.</p>
      </div>
    </article>
    <article class="blog-card">
      <div class="blog-photo mono-a" role="img" aria-label="Black and white photo of a family sitting on the beach"></div>
      <div class="blog-meta">
        <div class="date-box"><div class="day">30</div><div class="month">FEB</div></div>
        <p class="blog-excerpt">Lorem ipsum dolor sit amet cons am etur adipiscing elit.</p>
      </div>
    </article>
    <article class="blog-card">
      <div class="blog-photo mono-b" role="img" aria-label="Black and white photo of a smiling family together"></div>
      <div class="blog-meta">
        <div class="date-box"><div class="day">02</div><div class="month">MAR</div></div>
        <p class="blog-excerpt">Lorem ipsum dolor sit amet cons am etur adipiscing elit.</p>
      </div>
    </article>
  </div>
</section>

<footer class="site-footer">
  <nav class="footer-nav">
    <a class="is-active" href="#">Home</a><span class="sep">/</span>
    <a href="#">About Us</a><span class="sep">/</span>
    <a href="#">Get Involved</a><span class="sep">/</span>
    <a href="#">How Valtrix Works</a><span class="sep">/</span>
    <a href="#">Donor Eligibility</a><span class="sep">/</span>
    <a href="#">Contact Us</a><span class="sep">/</span>
    <a href="#">Terms of Use</a><span class="sep">/</span>
    <a href="#">Legal and Privacy Policy</a>
  </nav>
  <div class="contact-row">
    <div class="contact-item address">
      <span class="contact-icon"><svg width="30" height="34" viewBox="0 0 30 34"><path d="M15 26C9 18 7 15 7 11a8 8 0 0 1 16 0c0 4-2 7-8 15z" fill="none" stroke="#7cd9da" stroke-width="2"/><circle cx="15" cy="11" r="3" fill="none" stroke="#7cd9da" stroke-width="2"/><ellipse cx="15" cy="28" rx="12" ry="4" fill="none" stroke="#7cd9da" stroke-width="2"/></svg></span>
      <div><div class="contact-label">Address</div><div class="contact-value">480 Larkmoor Avenue, NW | Fairbrook, DC, 20019</div></div>
    </div>
    <div class="contact-item phone">
      <span class="contact-icon"><svg width="32" height="32" viewBox="0 0 32 32"><path d="M8 3l5 6-3 3c2 4 5 7 9 9l3-3 6 5-4 5C14 27 5 18 3 8z" fill="none" stroke="#7cd9da" stroke-width="2"/></svg></span>
      <div><div class="contact-label">Phone</div><div class="contact-value">202.555.0147</div></div>
    </div>
    <div class="contact-item email">
      <span class="contact-icon"><svg width="34" height="30" viewBox="0 0 34 30"><path d="M2 12 17 2l15 10v16H2z" fill="none" stroke="#7cd9da" stroke-width="2"/><path d="M2 12l15 10 15-10" fill="none" stroke="#7cd9da" stroke-width="2"/></svg></span>
      <div><div class="contact-label">Email</div><div class="contact-value">registration@valtrix.com</div></div>
    </div>
  </div>
  <div class="footer-bottom">
    <p>Copyright © 2016 Valtrix. All Rights Reserved.</p>
    <div class="social-footer">
      <a class="social-square is-teal" href="#" aria-label="Social profile"></a>
      <a class="social-square" href="#" aria-label="Social profile"></a>
      <a class="social-square" href="#" aria-label="Social profile"></a>
    </div>
  </div>
</footer>

</body>
</html>
```